Marrowfell Website Concept

We would like a one page website. Please refer to the attached files for more information.

Please reference file attachment version 1.1.

```html
<!DOCTYPE html>
<html lang="en">
<head>
<meta charset="utf-8">
<title>Marrowfell Security</title>
<link rel="stylesheet" href="https://fonts.googleapis.com/css2?family=Cinzel:wght@400;700&family=Open+Sans:wght@400;600;700&display=swap">
<style>
:root{
  --blue-top:#4a95d4;
  --blue-mid:#2f78c2;
  --blue-deep:#2361ad;
  --navy:#0b2546;
  --navy-ink:#112a4c;
  --btn-dark:#0f2747;
  --btn-blue:#1f5fa8;
  --link:#2a6bb5;
  --green:#7aa46b;
  --grey-text:#8a8a8a;
  --body-text:#666;
  --head-text:#333;
  --line:#dcdcdc;
  --footer:#171717;
  --white:#fff;
}
*{margin:0;padding:0;box-sizing:border-box}
html,body{width:1200px;height:2400px;overflow:hidden;background:var(--white)}
body{position:relative;font-family:"Open Sans",Arial,sans-serif;color:var(--body-text)}
.abs{position:absolute}
.serif{font-family:"Cinzel",Georgia,serif}

/* header */
.site-header{left:0;top:0;width:1200px;height:88px;background:linear-gradient(#5aa2dc,var(--blue-mid))}
.brand{display:flex;align-items:center;gap:10px}
.brand-dot{width:34px;height:34px;border-radius:50%;background:var(--navy-ink)}
.brand-name{font-family:"Cinzel",Georgia,serif;font-weight:700;font-size:29px;color:var(--navy-ink);letter-spacing:1px}
.header-brand{left:165px;top:24px}
.main-nav{left:461px;top:0;height:88px;display:flex}
.main-nav a{font-family:"Cinzel",Georgia,serif;font-size:13px;color:var(--white);text-decoration:none;line-height:92px;padding:0 14px}
.main-nav a.active{background:rgba(10,50,110,.35);width:77px;text-align:center;padding:0;margin-right:14px}

/* hero */
.hero{left:0;top:88px;width:1200px;height:365px;background:linear-gradient(90deg,#f4f5f7 0%,#eceef1 45%,#e6e8ec 70%,#f1f2f4 100%)}
.hero-photo{left:640px;top:64px;width:376px;height:248px;background:linear-gradient(#e3e4e6,#cfcfd1);border-radius:4px}
.hero-title{left:181px;top:58px;font-size:24px;color:#4a4a4a;letter-spacing:1px}
.hero-lead{left:184px;top:108px;width:340px;font-size:14px;font-weight:600;color:var(--navy-ink);line-height:21px}
.hero-text{left:181px;top:170px;width:330px;font-size:12px;line-height:19px;color:var(--grey-text)}
.btn{display:block;text-align:center;color:var(--white);font-size:12px;border-radius:4px;text-decoration:none;line-height:30px}
.btn-about{left:181px;top:296px;width:136px;background:var(--btn-dark)}
.btn-portfolio{left:341px;top:296px;width:134px;background:linear-gradient(#2c74c1,var(--btn-blue))}
.slider-arrow{top:160px;width:40px;height:40px;border-radius:50%;background:var(--white);border:2px solid #d6d8dc;display:flex;align-items:center;justify-content:center}

/* about */
.about{left:0;top:453px;width:1200px;height:291px;background:linear-gradient(var(--blue-mid),var(--blue-deep));color:var(--white);text-align:center}
.about-title{left:0;top:38px;width:1200px;font-size:22px;letter-spacing:1px}
.about-title svg{vertical-align:middle;margin:0 18px}
.about-text{left:195px;top:83px;width:810px;font-size:13.5px;line-height:25px}
.social{left:533px;top:178px;display:flex;gap:5px}
.social span{width:24px;height:24px;border-radius:50%;border:1.5px solid var(--white)}
.btn-more{left:538px;top:229px;width:129px;height:32px;line-height:32px;background:#1d5aa0;font-size:13.5px;font-weight:600;border-radius:2px;box-shadow:0 2px 0 rgba(0,0,0,.15)}

/* services */
.section-title{font-family:"Cinzel",Georgia,serif;color:#222;text-align:center;font-size:24px;letter-spacing:1px}
.services-title{left:0;top:778px;width:1200px}
.rule{height:1px;background:linear-gradient(90deg,transparent,#cfcfcf,transparent)}
.service-card{width:364px;height:142px;border:1.5px solid #e3e3e3;background:var(--white)}
.service-img{left:18px;top:22px;width:96px;height:96px;background:linear-gradient(#e8e8e8,#b9b9b9)}
.service-name{left:135px;top:25px;width:210px;font-size:14.5px;color:#333;line-height:16px}
.service-text{left:135px;top:54px;width:215px;font-size:10.5px;color:var(--grey-text);line-height:16px}
.service-text.lower{top:70px}
.service-link{left:135px;top:105px;font-size:11.5px;color:var(--link)}

/* solution */
.solution{left:0;top:1251px;width:1200px;height:394px;background:var(--navy)}
.solution-title{left:0;top:50px;width:1200px;color:var(--white);font-size:28px}
.solution-col{top:147px;width:210px;text-align:center}
.sol-icon{margin:0 auto;width:67px;height:67px;border-radius:50%;border:2px solid #7fae75;display:flex;align-items:center;justify-content:center}
.sol-label{font-family:"Cinzel",Georgia,serif;margin-top:28px;font-size:16px;color:var(--green);text-transform:none;font-family:Georgia,"Times New Roman",serif}
.sol-rule{margin:16px auto 0;width:200px;height:1.5px;background:#d6dbe3}
.sol-text{margin-top:14px;font-size:12px;line-height:16px;color:var(--white)}

/* people */
.people-title{left:226px;top:1695px;width:300px;font-size:28px}
.join-title{left:716px;top:1695px;width:300px;font-size:28px}
.person-avatar{width:99px;height:99px;border-radius:50%;border:3px solid #e4e4e4;background:linear-gradient(#c9c1b8,#8b7c70)}
.person-quote{left:307px;width:285px;font-size:12.5px;line-height:17px;color:#777}
.person-quote::before{content:"";position:absolute;left:-14px;top:0;height:92px;border-left:1px solid #ddd}
.person-name{font-family:"Cinzel",Georgia,serif;font-size:11px;color:var(--link);margin-top:9px}
.person-name small{font-family:"Open Sans",Arial,sans-serif;font-size:9px;color:#333}
.join-form{left:731px;top:1779px;width:280px;height:282px;background:#f7f7f7;border:1px solid #ececec}
.field{left:15px;width:251px;height:29px;background:var(--white);border:1px solid #e2e2e2;font-size:10px;font-style:italic;color:#999;padding:7px 10px}
.btn-send{left:79px;top:237px;width:126px;height:29px;line-height:29px;background:var(--btn-blue);font-size:15px;font-weight:600;border-radius:2px}

/* footer */
.site-footer{left:0;top:2136px;width:1200px;height:195px;background:var(--footer)}
.footer-nav{left:168px;top:38px;display:flex;gap:28px}
.footer-nav a{font-family:Georgia,"Times New Roman",serif;font-size:12px;color:var(--white);text-decoration:none}
.copyright{left:168px;top:74px;font-size:9.5px;color:#9a9a9a}
.news-title{left:552px;top:35px;font-family:"Cinzel",Georgia,serif;font-size:16px;color:#c9c9c9}
.news-input{left:552px;top:64px;width:152px;height:27px;background:var(--white);font-size:9.5px;font-style:italic;color:#999;padding:7px 10px}
.news-btn{left:706px;top:64px;width:84px;height:27px;line-height:27px;background:var(--btn-blue);border-radius:0;font-size:12px}
.footer-brand{left:855px;top:62px}
.footer-brand .brand-name{color:var(--white);font-size:22px}
.footer-brand .brand-dot{background:#2a6bb5;width:28px;height:28px}
</style>
</head>
<body>

<header class="site-header abs">
  <div class="brand header-brand abs"><span class="brand-dot"></span><span class="brand-name">Marrowfell</span></div>
  <nav class="main-nav abs">
    <a class="active" href="#">HOME</a><a href="#">FEATURES</a><a href="#">PAGES</a><a href="#">PORTOFOLIO</a><a href="#">BLOG</a><a href="#">SHOWCASE</a><a href="#">BUY IT</a>
  </nav>
</header>

<section class="hero abs">
  <div class="hero-photo abs" role="img" aria-label="Four business professionals seated on a white sofa in front of an office building"></div>
  <h1 class="hero-title abs serif">Welcome To Our security!</h1>
  <p class="hero-lead abs">Halcyon is flexible and clean business theme with lots of premium features</p>
  <p class="hero-text abs">Duis aute irure dolor in reprehenderit in voluptate velit esse cillum dolore eu fugiat nulla pariatur. Excepteur sint occaecat cupidatat non proident onum nibh euismod i quam ac diam pharetra mattis ut eget elit. Vestib ulum inerse pharetra dolor iquam ultrice rutrum libero utpulv.</p>
  <a class="btn btn-about abs" href="#">More About Us</a>
  <a class="btn btn-portfolio abs" href="#">View Portfolio</a>
  <div class="slider-arrow abs" style="left:33px"><svg width="12" height="12" viewBox="0 0 12 12"><path d="M8 2 L4 6 L8 10" stroke="#0b2546" stroke-width="2.5" fill="none"/></svg></div>
  <div class="slider-arrow abs" style="left:1126px"><svg width="12" height="12" viewBox="0 0 12 12"><path d="M4 2 L8 6 L4 10" stroke="#0b2546" stroke-width="2.5" fill="none"/></svg></div>
</section>

<section class="about abs">
  <h2 class="about-title abs serif">
    <svg width="88" height="14" viewBox="0 0 88 14"><path d="M0 8H60M50 3H88M60 8H88M60 12H88" stroke="#fff" stroke-width="1.5"/></svg>About Business<svg width="88" height="14" viewBox="0 0 88 14"><path d="M0 3H38M0 8H88M0 12H28" stroke="#fff" stroke-width="1.5"/></svg>
  </h2>
  <p class="about-text abs">Marrowfell Security, LLC is a United States-based tier one security firm specializing in the protection of financial services professionals, executives and their families. &nbsp;We manage engagements resulting from general and specific threats throughout the United States and abroad on behalf of our domestic clients.</p>
  <div class="social abs"><span></span><span></span><span></span><span></span><span></span></div>
  <a class="btn btn-more abs" href="#">Read More &#8853;</a>
</section>

<section class="services">
  <h2 class="section-title services-title abs">Searvice Offering</h2>
  <div class="rule abs" style="left:352px;top:829px;width:528px"></div>

  <article class="service-card abs" style="left:224px;top:875px">
    <div class="service-img abs" role="img" aria-label="Hooded figure working on a laptop"></div>
    <h3 class="service-name abs" style="font-weight:400">Threat Assessment</h3>
    <p class="service-text abs">Lorem ipsum dolor sit amet, consectetur adipisg elitm Ut tincidunt purus iaculis ipsum dctum non dtum quam sceleri</p>
    <a class="service-link abs">Read more</a>
  </article>
  <article class="service-card abs" style="left:616px;top:875px">
    <div class="service-img abs" role="img" aria-label="Pencil shaped like a light bulb" style="background:linear-gradient(#f2f2f2,#c8c8c8)"></div>
    <h3 class="service-name abs" style="font-weight:400">Threat Avoidance Plan &amp; Dossier Creation</h3>
    <p class="service-text lower abs">Lorem ipsum dolor sit amet, consectetur adipisg elitm Ut tincidunt purus iaculis</p>
    <a class="service-link abs">Read more</a>
  </article>
  <article class="service-card abs" style="left:224px;top:1043px">
    <div class="service-img abs" role="img" aria-label="Small figure pushing lettered blocks" style="background:linear-gradient(#f0f0f0,#bdbdbd)"></div>
    <h3 class="service-name abs" style="font-weight:400">Elite Executive Protection</h3>
    <p class="service-text abs">Lorem ipsum dolor sit amet, consectetur adipisg elitm Ut tincidunt purus iaculis ipsum dctum non dtum quam sceleri</p>
    <a class="service-link abs">Read more</a>
  </article>
  <article class="service-card abs" style="left:616px;top:1043px">
    <div class="service-img abs" role="img" aria-label="Child holding a small gavel" style="background:linear-gradient(#e9e9e9,#b7b0a8)"></div>
    <h3 class="service-name abs" style="font-weight:400">Threat Avoidance Plan &amp; Dossier Maintenance</h3>
    <p class="service-text lower abs">Lorem ipsum dolor sit amet, consectetur adipisg elitm Ut tincidunt purus iaculis</p>
    <a class="service-link abs">Read more</a>
  </article>
</section>

<section class="solution abs">
  <h2 class="section-title solution-title abs">OUR SOLUTION</h2>
  <div class="rule abs" style="left:320px;top:94px;width:560px;background:linear-gradient(90deg,transparent,#8fa3bf,transparent)"></div>

  <div class="solution-col abs" style="left:161px">
    <div class="sol-icon"><svg width="34" height="28" viewBox="0 0 34 28"><g fill="#fff"><rect x="1" y="1" width="32" height="7" rx="1"/><rect x="1" y="10.5" width="32" height="7" rx="1"/><rect x="1" y="20" width="32" height="7" rx="1"/></g><g fill="#0b2546"><rect x="4" y="3.5" width="10" height="2"/><rect x="4" y="13" width="10" height="2"/><rect x="4" y="22.5" width="10" height="2"/></g></svg></div>
    <div class="sol-label">Transfer Pricing &amp; IT</div><div class="sol-rule"></div>
    <p class="sol-text">Lorem Ipsum is simply dummy text of the printing and typesetting industry.</p>
  </div>
  <div class="solution-col abs" style="left:383px">
    <div class="sol-icon"><svg width="26" height="32" viewBox="0 0 26 32"><path d="M9 2 a2.5 2.5 0 0 1 5 0 V13 h6 a4 4 0 0 1 4 4 v7 a7 7 0 0 1 -7 7 h-5 a7 7 0 0 1 -7 -7 v-8 h4 z" fill="#fff"/></svg></div>
    <div class="sol-label">Request a fee quote</div><div class="sol-rule"></div>
    <p class="sol-text">Lorem Ipsum is simply dummy text of the printing and typesetting industry.</p>
  </div>
  <div class="solution-col abs" style="left:609px">
    <div class="sol-icon"><svg width="34" height="34" viewBox="0 0 34 34"><circle cx="17" cy="17" r="14" fill="none" stroke="#fff" stroke-width="2.5"/><rect x="2" y="13" width="30" height="8" fill="#fff"/><ellipse cx="17" cy="17" rx="6" ry="14" fill="none" stroke="#fff" stroke-width="2"/><path d="M5 16l1.5 3 1.5-3 1.5 3 1.5-3M13 16l1.5 3 1.5-3 1.5 3 1.5-3M21 16l1.5 3 1.5-3 1.5 3 1.5-3" stroke="#0b2546" stroke-width="1.2" fill="none"/></svg></div>
    <div class="sol-label">Network Partners</div><div class="sol-rule"></div>
    <p class="sol-text">Lorem Ipsum is simply dummy text of the printing and typesetting industry.</p>
  </div>
  <div class="solution-col abs" style="left:834px">
    <div class="sol-icon"><svg width="34" height="34" viewBox="0 0 34 34"><circle cx="17" cy="17" r="11" fill="none" stroke="#fff" stroke-width="5" stroke-dasharray="4 3"/><circle cx="17" cy="17" r="8" fill="#fff"/><circle cx="15" cy="15" r="4" fill="none" stroke="#0b2546" stroke-width="2"/><path d="M18 18l4 4" stroke="#0b2546" stroke-width="2.5"/></svg></div>
    <div class="sol-label">Pricing &amp; Tax Assurance</div><div class="sol-rule"></div>
    <p class="sol-text">Lorem Ipsum is simply dummy text of the printing and typesetting industry.</p>
  </div>
</section>

<section class="people">
  <h2 class="section-title people-title abs">PEOPLES</h2>
  <div class="rule abs" style="left:246px;top:1744px;width:270px"></div>
  <div class="person-avatar abs" style="left:176px;top:1787px" role="img" aria-label="Portrait of a smiling man in a suit"></div>
  <div class="person-quote abs" style="top:1779px">Lorem Ipsum is simply dummy text of the printing and typesetting industry. Lorem Ipsum has been the industry's standard dummy text ever since the 1500s, when an unknown printer took a galley of type and scrambled it to make a type specimen book.
    <div class="person-name">Arlen Voss <small>, DELHI</small></div></div>
  <div class="person-avatar abs" style="left:176px;top:1931px;background:linear-gradient(#f3e2d2,#d2a880)" role="img" aria-label="Portrait of a woman"></div>
  <div class="person-quote abs" style="top:1923px">Lorem Ipsum is simply dummy text of the printing and typesetting industry. Lorem Ipsum has been the industry's standard dummy text ever since the 1500s, when an unknown printer took a galley of type and scrambled it to make a type specimen book.
    <div class="person-name">Arlen Voss <small>, DELHI</small></div></div>

  <h2 class="section-title join-title abs">JOIN US</h2>
  <div class="rule abs" style="left:736px;top:1744px;width:270px"></div>
  <form class="join-form abs">
    <div class="field abs" style="top:17px">Name</div>
    <div class="field abs" style="top:54px">Email</div>
    <div class="field abs" style="top:90px">Phone number</div>
    <div class="field abs" style="top:126px">Property address</div>
    <div class="field abs" style="top:162px;height:62px">Message</div>
    <span class="btn btn-send abs">Send</span>
  </form>
</section>

<footer class="site-footer abs">
  <nav class="footer-nav abs"><a href="#">Home</a><a href="#">Solutions</a><a href="#">People</a><a href="#">Join us</a><a href="#">Contact Us</a></nav>
  <p class="copyright abs">Copyright © 2014.Vantrel Holdings. All Rights Reserved.</p>
  <h3 class="news-title abs" style="font-weight:400">Signup to Our Newsletters</h3>
  <div class="news-input abs">E-mail Address</div>
  <span class="btn news-btn abs">Subscribe</span>
  <div class="brand footer-brand abs"><span class="brand-dot"></span><span class="brand-name">Marrowfell</span></div>
</footer>

</body>
</html>
```